Purchasing Management Consulting B to B Web Design PAYMENT GUARANTY

We'd like to build a new digital image for our website.

Our company is managing purchasing consultancy services for Large and Medium companies around 4 activities :
- Procurement outsourcing
- Purchasing consulting (cost reduction)
- Supply chain training
- Web platform to manage Supplier risk (TrovaNorm.com)

We now aim to harmonies our website in term of design in order to build a strongest Corporate Image.

SEE REQUIREMENT ENCLOSED

Please have a look on our current websites:
- www.kelpstrand.com
- www.qtr-network.com
- www.trovanorm.com

Reason: Hello, Some project received are not really professional and need more details. I did not see all deliverable requested in specifications. I'll revert to designer to improve design. Regards, Gaspard

Reason: Only few designers reply and feedback still need to be done.

Target Market(s)

Our business is exclusively Business to Business toward Medium and Large companies.

Industry/Entity Type

Digital

Requirements
Must have
• Website will be developped in Joomla CMS.
The user community will use Jomsocial module : Visitor should be "influenced" to communicate its contact details by registering the community.

Ergonomy, Simplicity and professionnalism is the key objectives.

Deliverables :
- Corporate Home page including clear access to our 4 activities
- Dynamique banner
- Corporate article / contact pages (1 or 2)
- Activities home pages (x 4)
- Activity Catalog (Indesign for paper version)
Nice to have
• Integration of Design for our consulting and training catalog will be interesting.

Livechat design (the one of Pixelharbor.com is good)
Should not have
• Only psd

Not html

```html
<!DOCTYPE html>
<html lang="fr">
<head>
<meta charset="utf-8">
<title>Kelp Strand Consulting</title>
<link rel="stylesheet" href="https://fonts.googleapis.com/css2?family=Source+Sans+3:wght@400;600;700&family=Arimo:wght@400;700&display=swap">
<style>
:root{
  --yellow:#ecbc38;
  --yellow-bright:#f7d51a;
  --grey-band:#e0e0e0;
  --ink:#1d1d1d;
  --icon:#3d3d3d;
  --muted:#7a7a7a;
  --card:#fdf5e0;
  --card-shadow:#f1e3bd;
  --accent:#e8a10f;
  --footer:#f9ecd0;
  --white:#fff;
}
*{box-sizing:border-box;margin:0;padding:0}
html,body{width:1200px;height:992px;overflow:hidden;background:var(--white)}
body{position:relative;font-family:"Arimo",Arial,sans-serif;color:var(--ink)}
.abs{position:absolute}

/* header */
.brand{left:212px;top:44px;display:flex;align-items:center;gap:8px}
.brand-mark{width:14px;height:14px;border-radius:50%;background:var(--accent)}
.brand-name{font-family:"Source Sans 3",sans-serif;font-weight:700;font-size:30px;line-height:1;color:#6e6e6e}
.nav-band{left:340px;top:43px;width:658px;height:43px;background:linear-gradient(90deg,rgba(247,213,26,0) 0%,var(--yellow-bright) 22%,var(--yellow-bright) 60%,var(--yellow) 100%)}
.nav{right:214px;top:58px;display:flex;gap:28px;font-family:"Source Sans 3",sans-serif;font-weight:600;font-size:10.5px;color:#2a2a2a}
.login{left:646px;top:93px;display:flex;align-items:center;font-family:"Source Sans 3",sans-serif;font-size:9.5px;color:var(--muted)}
.login input{width:93px;height:24px;border:1px solid #d3d3d3;margin:0 8px}
.login button{width:41px;height:23px;border:1px solid #d7d7d7;background:#f4f4f4;color:#a0a0a0;font:inherit;font-size:9px}

/* activities */
.activities{left:0;top:127px;width:1200px;height:246px;background:var(--grey-band);border-bottom:1px solid #f4f4f4}
.activities h1{position:absolute;top:38px;width:100%;text-align:center;font-family:"Source Sans 3",sans-serif;font-weight:600;font-size:22px;color:#666}
.activity{position:absolute;top:106px;width:150px;text-align:center}
.activity svg{width:52px;height:52px;fill:var(--icon)}
.activity span{display:block;margin-top:17px;font-family:"Source Sans 3",sans-serif;font-weight:600;font-size:16px;color:#111}

/* feature */
.feature{left:0;top:374px;width:1200px;height:276px;background:var(--yellow)}
.feature-art{left:248px;top:38px;width:186px;height:196px;border-radius:6px;background:linear-gradient(180deg,#c9c9c9,#8c8c8c)}
.feature-text{left:496px;top:48px;width:480px}
.feature-text h2{font-family:"Source Sans 3",sans-serif;font-weight:700;font-size:17px;color:#111}
.feature-text p{font-size:9.5px;line-height:11.6px;color:#4a3a10;margin-top:8px}
.feature-text .lead{font-size:16.5px;line-height:20px;color:#5a4a20;margin-top:14px}
.feature-text .lead b{font-weight:400;color:#111}
.feature-text ul{list-style:none;margin:20px 0 0 18px;font-size:9.5px;line-height:11.6px;color:#4a3a10}
.feature-text li{position:relative;padding-left:15px;width:400px}
.feature-text li::before{content:"»";position:absolute;left:0;top:3px}

/* cards */
.card{top:672px;width:178px;height:204px;background:var(--card);box-shadow:4px 4px 0 var(--card-shadow);padding:0 6px 0 14px}
.card h3{margin:14px 8px 0 0;padding-bottom:8px;border-bottom:1px dotted #c9c0a8;text-align:center;font-weight:400;font-size:15px;color:#222}
.card p{font-size:9.5px;line-height:12px;margin-top:18px;color:#222}
.card .hl{color:var(--accent);font-weight:700}
.card .more{font-weight:700}
.card .note{font-weight:700;color:#555}
.partner{width:134px;height:75px;background:var(--white);margin-top:10px;display:flex;align-items:center;justify-content:center;gap:6px;font-weight:700;font-size:17px;color:#222}
.partner i{width:12px;height:12px;border-radius:50%;background:var(--accent)}
.email{width:154px;height:28px;border:1px solid #dcd3bb;background:var(--white);margin-top:11px;font-size:9.5px;color:#aaa;padding:8px 0 0 18px}
.subscribe{display:block;margin:10px 0 0 21px;width:112px;height:28px;border:1px solid #c98b00;border-radius:3px;background:linear-gradient(#f9d33a,#eaa400);color:var(--white);font-family:"Source Sans 3",sans-serif;font-weight:600;font-size:10.5px}
.social{display:flex;gap:3px;margin:20px 0 0 10px}
.social span{width:24px;height:24px;border-radius:3px}

/* footer */
.footer{left:0;top:902px;width:1200px;height:90px;background:var(--footer);text-align:center;font-size:9.5px;color:#222}
.footer .links{margin-top:18px;font-weight:700;color:#444}
.footer .legal{margin-top:10px;line-height:11.5px}
</style>
</head>
<body>

<header>
  <div class="abs nav-band"></div>
  <div class="abs brand"><span class="brand-mark"></span><span class="brand-name">KSC</span></div>
  <nav class="abs nav"><span>ACCUEIL</span><span>KELP STRAND</span><span>METIERS</span><span>NOS REFERENCES</span><span>CONTACT US</span></nav>
  <form class="abs login">USERNAME<input type="text">PASSWORD<input type="password"><button type="button">LOG IN</button></form>
</header>

<section class="abs activities">
  <h1>ACHETEZ EN TOUTE SIMPLICITE</h1>
  <div class="activity" style="left:213px">
    <svg viewBox="0 0 52 52"><path d="M0 13h18l21-11v49L18 40H0z"/><rect x="7" y="40" width="11" height="12" rx="3"/></svg>
    <span>COMMUNAUTE</span>
  </div>
  <div class="activity" style="left:367px">
    <svg viewBox="0 0 52 52"><path d="M0 0h33v26H14l-7 7v-7H0z"/><path d="M37 14h15v30h-6v8l-7-8H21V30h16z"/></svg>
    <span>CONSULTING</span>
  </div>
  <div class="activity" style="left:535px">
    <svg viewBox="0 0 52 52"><circle cx="34" cy="12" r="12"/><path d="M18 52V35c0-8 6-11 16-11s18 3 18 11v17z"/><circle cx="12" cy="18" r="7"/><path d="M0 52V37c0-6 4-9 13-9 3 0 3 2 3 4v20z"/></svg>
    <span>FORMATION</span>
  </div>
  <div class="activity" style="left:688px">
    <svg viewBox="0 0 52 52"><path d="M23 5a23 23 0 1 0 24 24H23z"/><path d="M28 0a24 24 0 0 1 24 24H28z"/></svg>
    <span>TROVANORM</span>
  </div>
  <div class="activity" style="left:842px">
    <svg viewBox="0 0 52 52"><rect width="13" height="13"/><rect x="19.5" width="13" height="13"/><rect x="39" width="13" height="13"/><rect y="19.5" width="13" height="13"/><rect x="19.5" y="19.5" width="13" height="13"/><rect x="39" y="19.5" width="13" height="13"/><rect y="39" width="13" height="13"/><rect x="19.5" y="39" width="13" height="13"/><rect x="39" y="39" width="13" height="13"/></svg>
    <span>MULTI-DEVIS</span>
  </div>
</section>

<section class="abs feature">
  <div class="abs feature-art" role="img" aria-label="Illustration area for the community feature"></div>
  <div class="abs feature-text">
    <h2>SED UT PERSPICIATIS UNDE OMNIS ISTE NATUS</h2>
    <p>Error sit voluptatem accusantium doloremque laudantium, totam rem aperiam, eaque ipsa quae ab illo inventore veritatis et quasi architecto beatae vitae dicta sunt explicabo. Nemo enim ipsam voluptatem quia voluptas sit aspernatur aut odit aut fugit, sed quia consequuntur magni dolores eos qui ratione voluptatem sequi nesciunt.</p>
    <p class="lead"><b>Error sit voluptatem accusantium</b> doloremque laudantium, totam rem aperiam, eaque ipsa quae ab illo inventore veritatis et quasi architecto beatae vitae dicta sunt explicabo.</p>
    <ul><li>Nemo enim ipsam voluptatem quia voluptas sit aspernatur aut odit aut fugit, sed quia dolores eos qui ratione voluptatem sequi nesciunt.</li></ul>
  </div>
</section>

<section class="abs card" style="left:215px">
  <h3>ACTUALITIES</h3>
  <p><span class="hl">Duis aute irure dolor in henderit</span><br>Excepteur sint occaecat cupidatat<br>non proident irure dolor in reprehen<br><span class="more">Read more..</span></p>
  <p><span class="hl">Duis aute irure dolor in henderit</span><br>Excepteur sint occaecat cupidatat<br>non proident irure dolor in reprehen<br><span class="more">Read more..</span></p>
  <svg class="abs" style="left:162px;top:178px" width="8" height="16" viewBox="0 0 8 16" fill="#888"><path d="M4 0l4 6H0zM4 16l4-6H0z"/></svg>
</section>

<section class="abs card" style="left:411px">
  <h3>KELP STRAND</h3>
  <p style="margin-top:14px">Duis aute irure dolor in reprehenderit<br>in voluptate velit esse cillum dolore<br>eu fugiat nulla pariatur. Excepteur<br>sint occaecat cupidatat non proident<br>irure dolor in reprehen</p>
  <p class="note" style="margin-top:12px">Excepteur sint occaecat cupidatat<br>non proident</p>
</section>

<section class="abs card" style="left:609px">
  <h3>PARTENARIATS</h3>
  <div class="partner"><i></i>ORVO WEAR</div>
  <p class="note" style="margin-top:12px">Excepteur sint occaecat cupida<br>non proident</p>
</section>

<section class="abs card" style="left:802px">
  <h3>NEWSLETTER</h3>
  <p style="margin-top:8px">Duis aute irure dolor in reprehenderi<br>in voluptate velit esse</p>
  <div class="email">enter your email here</div>
  <button class="subscribe" type="button">SUBSCRIBE</button>
  <div class="social">
    <span style="background:#8fd3f1"></span><span style="background:#9fdcec"></span><span style="background:#3b5c9c"></span><span style="background:#fff;border:1px solid #ddd"></span><span style="background:#333"></span>
  </div>
</section>

<footer class="abs footer">
  <div class="links">Mentions legales &nbsp;|&nbsp; Plan du site &nbsp;|&nbsp; Kelp Strand &nbsp;|&nbsp; Blog</div>
  <div class="legal">COPYRIGHT 2013. ALL RIGHTS RESERVED.<br>TERMS &amp; CONDITIONS &nbsp;- &nbsp; PRIVACY &nbsp; - &nbsp; DISCLAIMER</div>
</footer>

</body>
</html>
```